Online Prescription Eyeglass Lens Company Needs a Website

*Update new name to ClearPair. Thx

We are eye doctors with a lab that need a website for a new company based in Southern California called ClearPair. We replace old prescription lenses with new ones next day for most lenses. Patients select the lenses and give us the prescription. We then send a box with a prepaid shipping label. Place the frames in the box and drop them in the mail to our lab. We will custom make new lenses, fit them back into your frames and send them back to you. We would like to compete with www.vizora.com and offer affordable lenses for single vision, bifocal, progressive, sunglass lenses at an affordable price with next day shipping.
Updates

Hi Designers, We have a new name called ClearPair. Can we have the website design reflect the new name and we'll pick our favorites. Thx

Update: The new name is OptiNova . I have not made very many changes or feedback to the submissions because we were bidding for a .com. We won and our new name is OptiNova . This is the last name change.. Please have the website reflect the new name and I'll be providing feedback on the websites . ( I have a separate project for the logo people are working on, so don't worry about creating a logo). Look forward to the submissions. Thanks everyone.

Hi, Just leave the name as ClearPair for now. I will narrow down top designs tonight. Thx

Target Market(s)

Anyone that wears prescription or nonprescription glasses or sunglasses that want next day shipping.

Industry/Entity Type

Eyewear

Number of Pages Required

4 page

Font styles to use
Serif

Colors

Designer to choose colors to be used in the design.

Requirements
Must have
• I need a website that can compete with https://www.vizora.com/.
• We are different from vizora because we can offer same day service or next day shipping.
• It needs to have website that offers the lenses available listed below.
• Needs to be able to upload a prescription and payment feature.
• Pictures of different types of options with small info about each lens option.
• Template Pricing (just use numbers from $79-$179 for now)
• SINGLE VISION LENSES
• HIGH INDEX LENSES
• READING LENSES
• DIGITAL HD PROGRESSIVE LENSES
• RX & NON-RX SUNGLASSES
• RX & NON-RX POLARIZED SUNGLASSES
• COMPUTER LENSES
• TRANSITION LENSES
• BI-FOCAL LENSES

```html
<!DOCTYPE html>
<html lang="en">
<head>
<meta charset="utf-8">
<title>ClearPair – Prescription Lenses</title>
<link rel="stylesheet" href="https://fonts.googleapis.com/css2?family=Oswald:wght@400;500&family=Lora:wght@400;500&family=Jost:wght@400;500&display=swap">
<style>
:root{
  --purple:#2e2a8a;
  --purple-deep:#2b2479;
  --red:#e01f2b;
  --ink:#1d1d1d;
  --body:#444;
  --grey-bg:#f2f2f2;
  --white:#fff;
  --footer:#2c2c2c;
  --footer-bar:#141414;
}
*{box-sizing:border-box;margin:0;padding:0}
html,body{width:1200px;height:3704px;overflow:hidden}
body{position:relative;background:var(--grey-bg);font-family:"Jost",sans-serif;color:var(--ink)}
.abs{position:absolute}
.heading{font-family:"Oswald",sans-serif;font-weight:400;text-transform:uppercase;color:var(--purple);letter-spacing:.5px}
.heading .accent{color:var(--red)}
.btn{position:absolute;display:flex;align-items:center;height:40px;border:2px solid var(--red);background:var(--red);color:#fff;font-size:13px;font-family:"Jost",sans-serif}
.btn .plus{width:36px;height:100%;background:#fff;color:var(--red);display:flex;align-items:center;justify-content:center;font-size:24px;font-weight:500;clip-path:polygon(0 0,100% 0,80% 100%,0 100%)}
.btn .label{flex:1;text-align:center;padding-right:6px}
.btn.purple{background:var(--purple);border-color:var(--purple)}
.btn.purple .plus{color:var(--purple)}

/* header */
.site-header{top:0;left:0;width:1200px;height:89px;background:#fff;z-index:5}
.logo{left:118px;top:24px;font-family:"Oswald",sans-serif;font-size:30px;font-weight:500;color:var(--purple);letter-spacing:.5px}
.main-nav{left:468px;top:36px;display:flex;gap:0;font-size:13px;text-transform:uppercase}
.main-nav a{color:var(--ink);text-decoration:none;margin-right:50px}
.main-nav a.current{color:var(--purple);border-bottom:2px solid var(--purple);padding-bottom:2px}
.order-btn{left:938px;top:26px;width:142px;height:38px;background:var(--red);color:#fff;font-size:13px;display:flex;align-items:center;gap:12px;padding-left:6px}
.order-btn .cart{width:30px;height:28px;background:#fff;display:flex;align-items:center;justify-content:center}

/* hero */
.hero{top:89px;left:0;width:1200px;height:516px;overflow:hidden}
.hero-photo{position:absolute;inset:0;background:linear-gradient(90deg,#c79a6c 0%,#e0c09a 30%,#efdcc4 55%,#b97d4e 75%,#f4ece2 100%)}
.hero-title{left:118px;top:150px;font-family:"Lora",serif;font-size:46px;color:var(--purple-deep)}
.hero-sub{left:120px;top:212px;font-family:"Jost",sans-serif;font-size:26px;color:#222}
.hero-dots{left:118px;top:380px;display:flex;gap:5px}
.hero-dots span{width:13px;height:13px;border-radius:50%;border:2px solid var(--purple);background:#fff}
.hero-dots span.on{background:var(--purple)}

/* feature cards */
.feature-card{top:526px;width:306px;height:351px;background:#fff;border-top:7px solid var(--red);box-shadow:0 2px 10px rgba(0,0,0,.12);text-align:center;z-index:3}
.feature-card svg{position:absolute;left:50%;transform:translateX(-50%);top:30px}
.feature-card h3{position:absolute;top:123px;width:100%;font-family:"Oswald",sans-serif;font-weight:400;font-size:30px;color:var(--red)}
.feature-card p{position:absolute;top:186px;left:28px;right:28px;font-size:12px;line-height:19px;color:var(--body)}
.feature-card .btn{left:83px;top:294px;width:140px}

/* how it works */
.how{top:945px;left:0;width:1200px;height:555px;background:#fff;clip-path:polygon(0 42px,100% 0,100% 100%,0 100%)}
.how-photo{left:0;top:0;width:570px;height:100%;background:linear-gradient(90deg,#f4f4f4 0%,#ece3da 45%,#d9b79a 70%,#f2f2f2 100%)}
.how-title{left:632px;top:105px;font-size:33px}
.how-step{left:632px;width:470px;display:flex;gap:16px}
.how-step .ico{flex:none;width:44px;height:44px;border:2px solid var(--purple);border-radius:50%;display:flex;align-items:center;justify-content:center}
.how-step h4{font-size:15px;font-weight:500;margin-top:1px}
.how-step p{font-size:11.5px;line-height:17px;color:var(--body)}

/* products */
.products{top:1494px;left:0;width:1200px;height:830px;background:var(--grey-bg)}
.products-title{top:35px;width:100%;text-align:center;font-size:34px}
.product{width:226px;text-align:center}
.product .shot{height:176px}
.product h4{margin-top:20px;font-size:17px;font-weight:500}
.product .price{margin-top:14px;font-size:15px;color:var(--purple)}

/* difference */
.difference{top:2312px;left:0;width:1200px;height:420px;background:#fff;clip-path:polygon(0 0,100% 40px,100% 100%,0 calc(100% - 30px))}
.difference-title{top:56px;width:100%;text-align:center;font-size:27px;color:var(--purple)}
.offer{text-align:center;font-size:22px;color:#333}
.or-badge{left:574px;top:172px;width:48px;height:48px;border-radius:50%;background:var(--purple);border:3px solid #e5e3f5;color:#fff;font-family:"Oswald",sans-serif;font-size:18px;display:flex;align-items:center;justify-content:center}

/* our lenses */
.lenses{top:2716px;left:0;width:1200px;height:380px;background:var(--grey-bg)}
.lenses-title{left:119px;top:57px;font-size:34px}
.lenses-copy{left:119px;top:110px;width:560px;font-size:17px;line-height:26px;color:#222}
.lenses-price{left:119px;top:222px;font-size:16px;color:#222}
.lenses-photo{left:605px;top:40px;width:530px;height:320px;background:radial-gradient(ellipse at 45% 55%,#6f94b3 0%,#8aa9c2 38%,#f2f2f2 70%);transform:rotate(-12deg)}

/* reviews */
.reviews{top:3087px;left:0;width:1200px;height:420px;background:linear-gradient(90deg,#3a2f93 0%,#4a3ea0 20%,#35298a 45%,#463a9c 70%,#372b8c 100%);clip-path:polygon(0 30px,100% 0,100% 100%,0 100%)}
.reviews-title{top:75px;width:100%;text-align:center;font-size:34px;color:#fff}
.review-card{top:168px;width:306px;height:202px;background:#fff;border-radius:3px;text-align:center}
.review-card .avatar{position:absolute;left:50%;top:-40px;margin-left:-40px;width:80px;height:80px;border-radius:50%;background:linear-gradient(#f1c9a6,#d99a6c);border:3px solid #fff}
.review-card p{position:absolute;left:26px;right:26px;top:62px;font-size:12px;line-height:18px;color:var(--body)}
.review-card .q{color:#bbb;font-family:"Lora",serif;font-size:26px;line-height:0;vertical-align:-8px}
.review-card h5{position:absolute;bottom:16px;width:100%;font-weight:400;font-size:18px;color:#222}

/* footer */
.site-footer{top:3501px;left:0;width:1200px;height:153px;background:var(--footer)}
.footer-nav{top:36px;width:100%;display:flex;justify-content:center;gap:64px;font-size:13px;text-transform:uppercase}
.footer-nav a{color:#fff;text-decoration:none}
.footer-rule{top:78px;left:120px;width:960px;height:1px;background:#444}
.social{top:102px;width:100%;display:flex;justify-content:center;gap:10px}
.social span{width:20px;height:20px;border-radius:50%;background:#6d6d6d}
.copyright{top:3654px;left:0;width:1200px;height:50px;background:var(--footer-bar);color:#ccc;font-size:11px;display:flex;align-items:center;justify-content:center}
</style>
</head>
<body>

<header class="abs site-header">
  <div class="abs logo">CLEARPAIR</div>
  <nav class="abs main-nav">
    <a class="current" href="#">Home</a><a href="#">About Us</a><a href="#">Products</a><a href="#">FAQ'S</a><a href="#">Contact Us</a>
  </nav>
  <a class="abs order-btn">
    <span class="cart"><svg width="20" height="18" viewBox="0 0 20 18"><path d="M1 2h3l2 9h10l2-7H5" fill="none" stroke="#e01f2b" stroke-width="2"/><circle cx="8" cy="15" r="1.6" fill="#e01f2b"/><circle cx="15" cy="15" r="1.6" fill="#e01f2b"/></svg></span>
    Order Lenses
  </a>
</header>

<section class="abs hero">
  <div class="hero-photo" role="img" aria-label="Smiling woman adjusting black eyeglass frames on a warm blurred background"></div>
  <h1 class="abs hero-title">Complete Eyeglasses</h1>
  <div class="abs hero-sub">Starting At $79-$179</div>
  <a class="btn" style="left:118px;top:264px;width:158px;height:44px">
    <span class="plus"><svg width="20" height="18" viewBox="0 0 20 18"><path d="M1 2h3l2 9h10l2-7H5" fill="none" stroke="#e01f2b" stroke-width="2"/><circle cx="8" cy="15" r="1.6" fill="#e01f2b"/><circle cx="15" cy="15" r="1.6" fill="#e01f2b"/></svg></span>
    <span class="label">Shop Now</span>
  </a>
  <div class="abs hero-dots"><span class="on"></span><span></span><span></span></div>
</section>

<article class="abs feature-card" style="left:119px">
  <svg width="150" height="70" viewBox="0 0 150 70"><g fill="none" stroke="#2e2a8a" stroke-width="5"><path d="M10 22h40c2 18-6 28-20 28S8 40 10 22z"/><path d="M62 22h40c2 18-6 28-20 28S60 40 62 22z"/><path d="M50 26q6-5 12 0"/></g><circle cx="122" cy="22" r="22" fill="#fff" stroke="#e01f2b" stroke-width="2"/><text x="122" y="20" text-anchor="middle" font-family="Jost,sans-serif" font-size="13" fill="#e01f2b">20%</text><text x="122" y="34" text-anchor="middle" font-family="Jost,sans-serif" font-size="12" fill="#e01f2b">Off</text></svg>
  <h3>SPECIALS OFFERS</h3>
  <p>Lorem Ipsum is simply dummy text of the printing and typesetting industry. Lorem Ipsum has been the industry's standard dummy text ever since the Ipsum has been the industry's.</p>
  <a class="btn"><span class="plus">+</span><span class="label">Read More</span></a>
</article>

<article class="abs feature-card" style="left:447px">
  <svg width="110" height="70" viewBox="0 0 110 70"><g fill="none" stroke="#2e2a8a" stroke-width="4"><path d="M8 28h40c2 16-6 24-20 24S6 44 8 28z"/><path d="M62 28h40c2 16-6 24-20 24S60 44 62 28z"/><path d="M48 32q7-5 14 0M8 28l6-10M102 28l-6-10"/></g></svg>
  <h3>EYE WEAR</h3>
  <p>Lorem Ipsum is simply dummy text of the printing and typesetting industry. Lorem Ipsum has been the industry's standard dummy text ever since the Ipsum has been the industry's.</p>
  <a class="btn purple"><span class="plus">+</span><span class="label">Read More</span></a>
</article>

<article class="abs feature-card" style="left:775px">
  <svg width="90" height="80" viewBox="0 0 90 80"><g fill="none" stroke="#2e2a8a" stroke-width="3"><path d="M20 62l26-26 12 12-26 26z"/><path d="M46 36l8-8 12 12-8 8"/><path d="M54 28l10-10 12 12-10 10"/><circle cx="70" cy="18" r="12"/><path d="M14 50q-6 8 0 12q6-4 0-12z"/></g></svg>
  <h3>VISION CARE</h3>
  <p>Lorem Ipsum is simply dummy text of the printing and typesetting industry. Lorem Ipsum has been the industry's standard dummy text ever since the Ipsum has been the industry's.</p>
  <a class="btn"><span class="plus">+</span><span class="label">Read More</span></a>
</article>

<section class="abs how">
  <div class="abs how-photo" role="img" aria-label="Woman covering one eye in front of an eye chart"></div>
  <h2 class="abs heading how-title">How <span class="accent">ClearPair Works</span></h2>
  <div class="abs how-step" style="top:172px">
    <span class="ico"><svg width="26" height="14" viewBox="0 0 26 14"><g fill="none" stroke="#e01f2b" stroke-width="2"><rect x="1" y="3" width="10" height="9" rx="3"/><rect x="15" y="3" width="10" height="9" rx="3"/><path d="M11 6h4"/></g></svg></span>
    <div><h4>Pick Your Lenses</h4><p>Lorem Ipsum is simply dummy text of the printing and typesetting industry. Lorem Ipsum has been the industry's standard dummy.</p></div>
  </div>
  <div class="abs how-step" style="top:246px">
    <span class="ico"><svg width="24" height="22" viewBox="0 0 24 22"><g fill="none" stroke="#e01f2b" stroke-width="2"><rect x="2" y="7" width="20" height="13"/><path d="M2 7l4-5h12l4 5M9 12h6"/></g></svg></span>
    <div><h4>Send Us Your Frames</h4><p>Lorem Ipsum is simply dummy text of the printing and typesetting industry. Lorem Ipsum has been the industry's standard dummy.</p></div>
  </div>
  <div class="abs how-step" style="top:333px">
    <span class="ico"><svg width="26" height="14" viewBox="0 0 26 14"><g fill="none" stroke="#e01f2b" stroke-width="2"><circle cx="6" cy="7" r="5"/><circle cx="20" cy="7" r="5"/><path d="M11 7h4"/></g></svg></span>
    <div><h4>We Re Lens Your Glasses</h4><p>Lorem Ipsum is simply dummy text of the printing and typesetting industry. Lorem Ipsum has been the industry's standard dummy.</p></div>
  </div>
  <div class="abs how-step" style="top:412px">
    <span class="ico"><svg width="26" height="20" viewBox="0 0 26 20"><g fill="none" stroke="#e01f2b" stroke-width="2"><path d="M1 3h15v11H1zM16 7h5l4 4v3h-9"/><circle cx="6" cy="16" r="2"/><circle cx="20" cy="16" r="2"/></g></svg></span>
    <div><h4>Sight, Sealed, Delivered</h4><p>Lorem Ipsum is simply dummy text of the printing and typesetting industry. Lorem Ipsum has been the industry's standard dummy.</p></div>
  </div>
</section>

<section class="abs products">
  <h2 class="abs heading products-title">Our <span class="accent">Products</span></h2>
  <div class="abs product" style="left:119px;top:109px"><div class="shot" role="img" aria-label="Flowers seen through an eyeglass lens" style="background:linear-gradient(135deg,#b9c4c6,#e7d39a 50%,#8e9ea2)"></div><h4>Single Vision Lenses</h4><div class="price">$78.00</div></div>
  <div class="abs product" style="left:365px;top:109px"><div class="shot" role="img" aria-label="Woman wearing black glasses" style="background:linear-gradient(135deg,#d8d2cc,#c79a7e 55%,#5a4a44)"></div><h4>High Index Lenses</h4><div class="price">$120.00</div></div>
  <div class="abs product" style="left:610px;top:109px"><div class="shot" role="img" aria-label="Reading glasses resting on an open book" style="background:linear-gradient(135deg,#3a2c24,#d8c8ac 50%,#efe6d4)"></div><h4>Reading Lenses</h4><div class="price">$92.00</div></div>
  <div class="abs product" style="left:854px;top:109px"><div class="shot" role="img" aria-label="Progressive lens view over a landscape" style="background:linear-gradient(180deg,#7aa6d4,#c7d6d8 45%,#6f8f4a)"></div><h4>Digital Hd Progressive Lenses</h4><div class="price">$135.00</div></div>
  <div class="abs product" style="left:119px;top:392px"><div class="shot" role="img" aria-label="Woman wearing sunglasses" style="background:linear-gradient(135deg,#6a4a34,#d2a580 50%,#3e2a20)"></div><h4>Rx &amp; Non-Rx Sunglasses</h4><div class="price">$78.00</div></div>
  <div class="abs product" style="left:365px;top:392px"><div class="shot" role="img" aria-label="Black glasses on a notebook with a pen" style="background:linear-gradient(135deg,#f2f2f0,#dcdcd8 55%,#9a9a96)"></div><h4>Rx &amp; Non-rx Polarized Sunglasses</h4><div class="price">$120.00</div></div>
  <div class="abs product" style="left:610px;top:392px"><div class="shot" role="img" aria-label="Computer glasses on a lilac surface" style="background:linear-gradient(135deg,#cbc3d3,#b3a8c2 50%,#d9d2e0)"></div><h4>Computer Lenses</h4><div class="price">$92.00</div></div>
  <div class="abs product" style="left:854px;top:392px"><div class="shot" role="img" aria-label="Man wearing transition lenses outdoors" style="background:linear-gradient(135deg,#8a9a6a,#c9b49a 50%,#4d5a3a)"></div><h4>Transition Lenses</h4><div class="price">$135.00</div></div>
  <a class="btn" style="left:536px;top:672px;width:128px;height:36px"><span class="plus">+</span><span class="label">View All</span></a>
</section>

<section class="abs difference">
  <h2 class="abs heading difference-title">We Are Different From vizora Because We Can Offer</h2>
  <div class="abs offer" style="left:320px;top:118px;width:200px">
    <svg width="120" height="124" viewBox="0 0 120 124"><text x="40" y="22" font-family="Oswald,sans-serif" font-size="19" fill="#e01f2b">Same</text><text x="44" y="42" font-family="Oswald,sans-serif" font-size="19" fill="#e01f2b">Day</text><path d="M28 56a40 40 0 1 0 20-12" fill="none" stroke="#e01f2b" stroke-width="7"/><path d="M40 38l12 6-10 10z" fill="#e01f2b"/><path d="M62 62v24h16" fill="none" stroke="#e01f2b" stroke-width="6"/></svg>
    <div style="margin-top:8px">Same Day Service</div>
  </div>
  <div class="abs or-badge">Or</div>
  <div class="abs offer" style="left:660px;top:118px;width:220px">
    <svg width="160" height="124" viewBox="0 0 160 124"><g fill="#e01f2b"><rect x="40" y="42" width="72" height="52"/><path d="M114 56h22l16 18v20h-38z"/><circle cx="62" cy="100" r="10"/><circle cx="132" cy="100" r="10"/><rect x="4" y="50" width="30" height="6"/><rect x="12" y="64" width="22" height="6"/><rect x="20" y="78" width="14" height="6"/></g><circle cx="62" cy="100" r="4" fill="#fff"/><circle cx="132" cy="100" r="4" fill="#fff"/><path d="M122 62h12l10 12h-22z" fill="#fff"/></svg>
    <div style="margin-top:8px">Next Day Shipping</div>
  </div>
</section>

<section class="abs lenses">
  <div class="abs lenses-photo" role="img" aria-label="Round glasses lying on a denim glasses case"></div>
  <h2 class="abs heading lenses-title">Our <span class="accent">Lenses</span></h2>
  <p class="abs lenses-copy">Lorem ipsum dolor sit amet, consectetuer adipiscing elit, sed diam nonummy nibh euismod tincidunt ut laoreet dolore magna aliquam erat volutpat. Ut wisi enim ad minim veniam, quis nostrud exerci tation ullamcorper suscipit lobortis nisl ut aliquip ex.</p>
  <div class="abs lenses-price">our lenses Prices starts from $79-$179</div>
  <a class="btn" style="left:119px;top:283px;width:226px;height:38px"><span class="plus">+</span><span class="label">Learn About Our Lenses</span></a>
</section>

<section class="abs reviews">
  <h2 class="abs heading reviews-title">Customer Reviews</h2>
  <article class="abs review-card" style="left:119px">
    <div class="avatar" role="img" aria-label="Customer avatar"></div>
    <p><span class="q">“</span> Lorem Ipsum simply dummy text of the printing and typesetting industry. Lorem Ipsum has been the industry's standard dummy text ever since the 1500s, when an unknown printer took a galley of type specimen book. <span class="q">”</span></p>
    <h5>LOREM IPSUM</h5>
  </article>
  <article class="abs review-card" style="left:447px">
    <div class="avatar" role="img" aria-label="Customer avatar"></div>
    <p><span class="q">“</span> Lorem Ipsum simply dummy text of the printing and typesetting industry. Lorem Ipsum has been the industry's standard dummy text ever since the 1500s, when an unknown printer took a galley of type specimen book. <span class="q">”</span></p>
    <h5>LOREM IPSUM</h5>
  </article>
  <article class="abs review-card" style="left:775px">
    <div class="avatar" role="img" aria-label="Customer avatar"></div>
    <p><span class="q">“</span> Lorem Ipsum simply dummy text of the printing and typesetting industry. Lorem Ipsum has been the industry's standard dummy text ever since the 1500s, when an unknown printer took a galley of type specimen book. <span class="q">”</span></p>
    <h5>LOREM IPSUM</h5>
  </article>
</section>

<footer class="abs site-footer">
  <nav class="abs footer-nav"><a href="#">Home</a><a href="#">About Us</a><a href="#">Products</a><a href="#">FAQ'S</a><a href="#">Contact Us</a></nav>
  <div class="abs footer-rule"></div>
  <div class="abs social"><span></span><span></span><span></span><span></span><span></span><span></span></div>
</footer>
<div class="abs copyright">Copyright © 2017 ClearPair. All Rights Reserved.</div>

</body>
</html>
```